Australian HR Consultancy Company Brochure (and more!). Our tagline "Start something amazing."

We are a start-up HR and Recruitment consultancy. We have a group of young, passionate and top performing staff who assist companies with driving their workforce productivity, keeping employees happy, hiring fantastic people and ensuring legal compliance across the HR field.

We work across a variety of sectors such as mining, Not for Profits, Finance, Accounting, Health etc so are not pigeon-holed to one particular group. We tend to deal with medium sized businesses.

Our team is professional and corporate but down to earth and approachable. We have unique offerings in terms of our services and our pricing. We deliver exceptional value to our clients and build long term mutually beneficial relationships. We care about giving back to the community and doing the right thing by everyone we deal with.

Our design should communicate that we are corporate and professional but not uptight 'suits', that we are fresh and engaging. Clear, concise, crisp but not cold.

Thinking 6 page brochure.

We have a variety of colours in our logo and tend to lean towards fresh shades of blue and green but are definitely open to other colours such as purple, pink, orange etc. We would prefer the brochure to be in landscape format (like a powerpoint presentation) as apparently that's easier to read? but open to your expert suggestions!

Target Market(s)

Medium sized business across all industries but within the professional area ie finance, mining, health.

Industry/Entity Type

It Company

Colors
33b8a4
33a6d7
0592cd
85cae6
86cfc6
b768aa

Requirements
Must have
• Needs to be editable version as we will be changing our tagline and about us in the new year.

```html
<!DOCTYPE html>
<html lang="en">
<head>
<meta charset="utf-8">
<title>TeamSpark Trifold Outside</title>
<link rel="stylesheet" href="https://fonts.googleapis.com/css2?family=Roboto:wght@400;500;700&family=Roboto+Condensed:wght@400;700&display=swap">
<style>
  :root {
    --canvas: #e6e6e6;
    --paper: #ffffff;
    --blue: #29a3d6;
    --blue-deep: #1c86b8;
    --blue-light: #5cc3ea;
    --grey: #808080;
    --grey-dark: #5e5e5e;
    --grey-soft: #d9d9d9;
    --purple: #8e2f8f;
    --orange: #ef7d1f;
    --navy: #1d4f7a;
    --ink: #3a3a3a;
    --body-font: "Roboto", Arial, sans-serif;
    --head-font: "Roboto Condensed", "Arial Narrow", sans-serif;
  }
  * { box-sizing: border-box; margin: 0; padding: 0; }
  html, body { width: 1200px; height: 1200px; overflow: hidden; background: var(--canvas); }
  body { font-family: var(--body-font); color: var(--ink); }

  .trifold {
    position: absolute; left: 60px; top: 195px;
    width: 1080px; height: 810px;
    display: flex;
    box-shadow: 0 6px 24px rgba(0,0,0,.12);
  }
  .panel {
    position: relative; width: 360px; height: 810px;
    background: var(--paper); overflow: hidden;
  }
  .panel + .panel { border-left: 1px solid #ececec; }
  .panel-art { position: absolute; inset: 0; width: 360px; height: 810px; }

  /* brand lockup */
  .brand { position: absolute; display: flex; align-items: center; gap: 10px; }
  .brand-dot { width: 34px; height: 34px; border-radius: 50%; background: var(--blue); }
  .brand-name { font-family: var(--body-font); font-weight: 500; font-size: 30px; color: var(--ink); letter-spacing: -.5px; }

  /* inside flap */
  .pill {
    position: absolute; left: 0; height: 24px; padding: 0 20px 0 20px;
    background: var(--blue); color: #fff; border-radius: 0 12px 12px 0;
    font-family: var(--head-font); font-size: 14px; line-height: 24px;
  }
  .about-copy {
    position: absolute; left: 20px; top: 128px; width: 320px;
    font-size: 10.5px; line-height: 1.45; text-align: justify; color: #444;
  }
  .about-copy p + p { margin-top: 10px; }
  .service-list { position: absolute; left: 20px; top: 346px; list-style: none; }
  .service-list li {
    display: flex; align-items: center; gap: 8px;
    font-family: var(--head-font); font-size: 14.5px; color: #333; margin-bottom: 13px;
  }
  .service-icon { width: 14px; height: 14px; }
  .flap-web {
    position: absolute; left: 0; right: 0; top: 770px; text-align: center;
    font-size: 11px; letter-spacing: 2px; color: #e8e8e8;
  }

  /* back panel */
  .headline {
    position: absolute; left: 0; right: 0; top: 190px; text-align: center; line-height: 1.18;
  }
  .headline .strong { font-family: var(--head-font); font-weight: 700; font-size: 26px; display: block; }
  .headline .soft { font-family: var(--body-font); font-size: 24px; color: #555; display: block; }
  .headline .purple { color: var(--purple); }
  .headline .orange { color: var(--orange); }
  .headline .blue { color: var(--blue-deep); }
  .contact-list { position: absolute; left: 24px; top: 700px; list-style: none; }
  .contact-list li { display: flex; align-items: center; gap: 9px; font-size: 11.5px; color: #222; margin-bottom: 12px; }
  .contact-icon { width: 13px; height: 13px; }

  /* cover */
  .cover-title {
    position: absolute; left: 0; right: 0; top: 640px; text-align: center;
  }
  .cover-name { font-family: var(--body-font); font-weight: 500; font-size: 33px; color: var(--purple); letter-spacing: 1px; }
  .cover-tagline { font-family: var(--head-font); font-weight: 700; font-size: 20px; color: var(--navy); margin-top: 2px; }
  .cover-phone {
    position: absolute; left: 0; right: 0; top: 730px; display: flex; justify-content: center; align-items: center; gap: 8px;
    font-size: 21px; color: #333;
  }
  .cover-phone svg { width: 17px; height: 17px; }
  .cover-web {
    position: absolute; left: 0; right: 0; top: 772px; text-align: center;
    font-size: 11px; letter-spacing: 4px; color: #222;
  }
</style>
</head>
<body>
<main class="trifold">

  <!-- Inside flap -->
  <section class="panel panel-flap">
    <svg class="panel-art" viewBox="0 0 360 810" aria-hidden="false">
      <polygon points="0,0 250,0 0,62" fill="var(--grey)"/>
      <polygon points="0,62 250,0 360,0 360,8 0,98" fill="var(--blue)"/>
      <polygon points="120,32 250,0 300,0 160,34" fill="var(--blue-light)"/>
      <polygon points="0,700 360,600 360,810 0,810" fill="var(--grey-dark)"/>
      <polygon points="0,640 360,560 360,610 0,700" fill="var(--blue)"/>
      <polygon points="180,468 296,535 296,669 180,736 64,669 64,535" fill="var(--grey-dark)"/>
      <polygon role="img" aria-label="Photo of a smiling team giving thumbs up"
        points="180,482 284,542 284,662 180,722 76,662 76,542" fill="url(#teamTone)"/>
      <defs>
        <linearGradient id="teamTone" x1="0" y1="0" x2="1" y2="1">
          <stop offset="0" stop-color="#e9e4df"/>
          <stop offset=".5" stop-color="#c9b4a5"/>
          <stop offset="1" stop-color="#eef0f3"/>
        </linearGradient>
      </defs>
    </svg>
    <div class="pill" style="top:88px">About Us :</div>
    <div class="about-copy">
      <p>TeamSpark is an innovative industry leader in the provision of human resources, industrial relations and recruitment managed services. Our unique approach enables us to meet the challenges and demands of a diverse group of contemporary Australian businesses.</p>
      <p>We are committed to delivering exceptional service and value that ensures the best outcomes for our long-term business partnerships.</p>
    </div>
    <div class="pill" style="top:304px">Our Services:</div>
    <ul class="service-list">
      <li><svg class="service-icon" viewBox="0 0 14 14"><circle cx="7" cy="7" r="6" fill="none" stroke="#777" stroke-width="1.2"/><path d="M4 7.2l2 2 4-4.4" fill="none" stroke="#777" stroke-width="1.3"/></svg>Hr consulting &amp; support</li>
      <li><svg class="service-icon" viewBox="0 0 14 14"><circle cx="7" cy="7" r="6" fill="none" stroke="#777" stroke-width="1.2"/><path d="M4 7.2l2 2 4-4.4" fill="none" stroke="#777" stroke-width="1.3"/></svg>Hr templates &amp; contracts</li>
      <li><svg class="service-icon" viewBox="0 0 14 14"><circle cx="7" cy="7" r="6" fill="none" stroke="#777" stroke-width="1.2"/><path d="M4 7.2l2 2 4-4.4" fill="none" stroke="#777" stroke-width="1.3"/></svg>Tailored Recruitment</li>
    </ul>
    <div class="flap-web">www.teamsparkhr.com.au</div>
  </section>

  <!-- Back panel -->
  <section class="panel panel-back">
    <svg class="panel-art" viewBox="0 0 360 810">
      <defs>
        <linearGradient id="officeTone" x1="0" y1="0" x2="0" y2="1">
          <stop offset="0" stop-color="#efefef"/>
          <stop offset=".6" stop-color="#f6f6f6"/>
          <stop offset="1" stop-color="#e4e4e4"/>
        </linearGradient>
      </defs>
      <rect role="img" aria-label="Faded photo of a modern office interior" x="0" y="0" width="360" height="640" fill="url(#officeTone)"/>
      <polygon points="0,650 360,520 360,810 0,810" fill="var(--paper)"/>
      <polygon points="215,565 360,515 360,645" fill="var(--grey)"/>
      <polygon points="0,565 360,425 360,515 0,650" fill="var(--blue)"/>
      <polygon points="0,600 200,522 360,470 360,515 0,650" fill="var(--blue-deep)" opacity=".55"/>
    </svg>
    <div class="headline">
      <span class="strong purple">WE HELP</span>
      <span class="soft">organisations reach</span>
      <span class="strong orange">THEIR FULL POTENTIAL</span>
      <span class="soft">through the power</span>
      <span class="strong blue">OF THEIR PEOPLE</span>
    </div>
    <div class="brand" style="left:24px; top:640px">
      <span class="brand-dot"></span><span class="brand-name">TeamSpark</span>
    </div>
    <ul class="contact-list">
      <li><svg class="contact-icon" viewBox="0 0 14 14"><path d="M7 1a4 4 0 0 0-4 4c0 3 4 8 4 8s4-5 4-8a4 4 0 0 0-4-4z" fill="var(--navy)"/><circle cx="7" cy="5" r="1.5" fill="#fff"/></svg>Perth | Melbourne | Sydney | Brisbane | Adelaide</li>
      <li><svg class="contact-icon" viewBox="0 0 14 14"><path d="M3 1.5l2.2 2.6-1.3 1.6c.8 1.7 2 2.9 3.7 3.7l1.6-1.3 2.6 2.2-1.3 1.9C6 11.6 2.4 8 1.1 2.8z" fill="none" stroke="var(--navy)" stroke-width="1.1"/></svg>1300 555 019</li>
      <li><svg class="contact-icon" viewBox="0 0 14 14"><circle cx="7" cy="7" r="5.8" fill="none" stroke="var(--navy)" stroke-width="1.1"/><path d="M1.2 7h11.6M7 1.2c-3 3.5-3 8.1 0 11.6M7 1.2c3 3.5 3 8.1 0 11.6" fill="none" stroke="var(--navy)" stroke-width="1"/></svg>www.teamsparkhr.com.au</li>
    </ul>
  </section>

  <!-- Cover -->
  <section class="panel panel-cover">
    <svg class="panel-art" viewBox="0 0 360 810">
      <defs>
        <linearGradient id="peopleTone" x1="0" y1="0" x2="0" y2="1">
          <stop offset="0" stop-color="#ffffff"/>
          <stop offset=".35" stop-color="#c7cbd3"/>
          <stop offset="1" stop-color="#3a4456"/>
        </linearGradient>
      </defs>
      <rect role="img" aria-label="Photo of four smiling business people in suits" x="20" y="115" width="320" height="460" fill="url(#peopleTone)"/>
      <polygon points="0,440 360,560 360,810 0,810" fill="var(--paper)"/>
      <polygon points="0,440 120,480 0,580" fill="var(--grey)"/>
      <polygon points="0,440 360,560 360,628 0,505" fill="var(--blue)"/>
      <polygon points="0,440 200,507 360,560 360,590 0,475" fill="var(--blue-deep)" opacity=".55"/>
      <polygon points="110,530 360,590 360,628" fill="var(--blue-light)" opacity=".6"/>
    </svg>
    <div class="brand" style="left:58px; top:52px">
      <span class="brand-dot"></span><span class="brand-name">TeamSpark</span>
    </div>
    <div class="cover-title">
      <div class="cover-name">TEAMSPARK</div>
      <div class="cover-tagline">START SOMETHING AMAZING</div>
    </div>
    <div class="cover-phone">
      <svg viewBox="0 0 14 14"><path d="M3 1.5l2.2 2.6-1.3 1.6c.8 1.7 2 2.9 3.7 3.7l1.6-1.3 2.6 2.2-1.3 1.9C6 11.6 2.4 8 1.1 2.8z" fill="none" stroke="var(--navy)" stroke-width="1.2"/></svg>
      1300 555 019
    </div>
    <div class="cover-web">www.teamsparkhr.com.au</div>
  </section>

</main>
</body>
</html>
```